Extremely Professional Lawyer needs letterhead for new boutique real estate law firm

I need letterhead for my new solo practice law firm. I practiced as a partner in a huge global law firm for years. Now I am starting a solo firm where I will deliver very high-quality legal services that are real-estate focused. The idea is that my practice will be very focused but that the services will be at the quality level provided by partners at high-profile law firms. The name of my law firm will be Brenner Law Group, LLC. For now, I am the only lawyer. I expect to negotiate and draft house sale/purchase contracts and close house deals. Eventually, I would like to do small-scale development deals for developer clients, a specialty of mine.

Industry/Entity Type

Boutique

```html
<!DOCTYPE html>
<html lang="en">
<head>
<meta charset="utf-8">
<title>Brenner Law Group, LLC — Letterhead</title>
<link href="https://fonts.googleapis.com/css2?family=Tinos&display=swap" rel="stylesheet">
<style>
  :root {
    --canvas: #ffffff;
    --ink: #231f20;
    --rule: #3a3a3a;
    --navy: #2b3a7e;
  }
  * { margin: 0; padding: 0; box-sizing: border-box; }
  html, body {
    width: 1200px;
    height: 1000px;
    overflow: hidden;
    background: var(--canvas);
  }
  .letterhead {
    position: absolute;
    left: 284px;
    top: 28px;
    width: 667px;
    height: 944px;
    border: 1px solid var(--rule);
    background: var(--canvas);
    font-family: "Tinos", "Times New Roman", serif;
    color: var(--ink);
  }
  .brand {
    position: absolute;
    left: 26px;
    top: 24px;
    display: flex;
    align-items: center;
  }
  .brand-square {
    width: 58px;
    height: 58px;
    background: var(--navy);
  }
  .brand-divider {
    width: 1px;
    height: 86px;
    background: var(--ink);
    margin-left: 12px;
    margin-right: 6px;
  }
  .brand-name {
    font-weight: 400;
    color: var(--ink);
    line-height: 1;
  }
  .brand-name .line-one {
    display: block;
    font-size: 40px;
    letter-spacing: 0.2px;
  }
  .brand-name .line-two {
    display: block;
    font-size: 31px;
    margin-top: 6px;
  }
  .contact {
    position: absolute;
    left: 0;
    right: 0;
    bottom: 15px;
    text-align: center;
    font-size: 12.5px;
    line-height: 16px;
    color: var(--ink);
  }
  .contact .sep { margin: 0 4px; }
</style>
</head>
<body>
  <div class="letterhead">
    <header class="brand">
      <div class="brand-square" aria-hidden="true"></div>
      <div class="brand-divider" aria-hidden="true"></div>
      <h1 class="brand-name">
        <span class="line-one">Brenner Law</span>
        <span class="line-two">Group, LLC</span>
      </h1>
    </header>
    <footer class="contact">
      <p class="contact-address">2140 W. Larkin Ave., Chicago, IL 60614</p>
      <p class="contact-lines">Ph: 312-555-0148<span class="sep">&#9679;</span>E- mail:mara@marabrennerlaw.com <span class="sep">&#9679;</span>Web:marabrennerlaw.com</p>
    </footer>
  </div>
</body>
</html>
```